Brevik Fabrication - Business Card Design

We would like a dark (likely black) themed business card to be able to hand out to potential clients. We may list our services on the card or keep it clean. Unsure. Logo attached

```html
<!DOCTYPE html>
<html lang="en">
<head>
<meta charset="utf-8">
<title>Brevik Fabrication – Business Card</title>
<link rel="stylesheet" href="https://fonts.googleapis.com/css2?family=Poppins:wght@400;500;600;700&display=swap">
<style>
  :root {
    --page: #1c1c1c;
    --card: #161616;
    --card-edge: #202020;
    --orange: #ef6a2c;
    --blue: #2a78c8;
    --white: #f2f2f2;
    --muted: #d9d9d9;
    --gloss: #3a3a3a;
  }
  * { margin: 0; padding: 0; box-sizing: border-box; }
  html, body { width: 1200px; height: 1200px; overflow: hidden; }
  body {
    background: var(--page);
    font-family: "Poppins", sans-serif;
    color: var(--white);
    position: relative;
  }
  .card {
    position: absolute;
    left: 170px;
    width: 860px;
    height: 491px;
    background: linear-gradient(160deg, var(--card-edge), var(--card) 60%);
    border-radius: 18px;
    box-shadow: 0 20px 40px rgba(0,0,0,.55);
    text-align: center;
  }
  .card--back { top: 70px; }
  .card--front { top: 640px; }

  .brand { display: flex; flex-direction: column; align-items: center; gap: 10px; }
  .brand__mark { width: 70px; height: 70px; border-radius: 50%; }
  .brand__name {
    font-weight: 700;
    font-size: 40px;
    letter-spacing: 1px;
    line-height: 1.1;
    text-transform: uppercase;
  }

  .card--back .brand { margin-top: 120px; }
  .card--back .brand__mark { background: var(--gloss); }
  .card--back .brand__name { color: var(--gloss); }
  .tagline-repeat {
    margin-top: 34px;
    font-size: 17px;
    line-height: 1.5;
    color: var(--white);
  }
  .tagline-repeat .dot {
    display: inline-block;
    width: 11px; height: 11px;
    border-radius: 50%;
    background: var(--orange);
    margin: 0 8px;
    vertical-align: middle;
  }

  .card--front .brand { margin-top: 62px; }
  .card--front .brand__mark { background: var(--orange); }
  .card--front .brand__name { color: var(--blue); }

  .person { margin-top: 22px; }
  .person__name {
    color: var(--orange);
    font-weight: 700;
    font-size: 28px;
    letter-spacing: 2px;
    text-transform: uppercase;
    line-height: 1.1;
  }
  .person__role { font-weight: 500; font-size: 19px; color: var(--white); }

  .contact {
    margin-top: 26px;
    display: flex;
    justify-content: center;
    align-items: stretch;
    gap: 18px;
    font-size: 18px;
    line-height: 1.4;
  }
  .contact__address { text-align: right; color: var(--muted); }
  .contact__rule { width: 1.5px; background: var(--muted); }
  .contact__lines { text-align: left; color: var(--muted); }
  .contact__label { color: var(--orange); margin-right: 6px; }
</style>
</head>
<body>
  <section class="card card--back">
    <div class="brand">
      <span class="brand__mark"></span>
      <span class="brand__name">Brevik Fabrication Inc</span>
    </div>
    <p class="tagline-repeat">
      Brevikfabrication<span class="dot"></span>Brevikfabrication<span class="dot"></span>Brevikfabrication<br>
      Brevikfabrication<span class="dot"></span>Brevikfabrication
    </p>
  </section>

  <section class="card card--front">
    <div class="brand">
      <span class="brand__mark"></span>
      <span class="brand__name">Brevik Fabrication Inc</span>
    </div>
    <div class="person">
      <p class="person__name">Dana Keller</p>
      <p class="person__role">Managing Director</p>
    </div>
    <div class="contact">
      <p class="contact__address">118 Harbor Street<br>Suite 210, Lakeview, MI 49000</p>
      <span class="contact__rule"></span>
      <p class="contact__lines">
        <span class="contact__label">P :</span>07950 318 642<br>
        <span class="contact__label">E :</span>dana@brevikfabrication.com<br>
        <span class="contact__label">W :</span>brevikfabrication.com
      </p>
    </div>
  </section>
</body>
</html>
```